Folder Ad

**Positive feedback for ALL submissions**

7.5"w X 4.5" h ad for:
Vault 4 Keep Storage, 4817 Brenmor ave, Saskatoon, SK, S4N 2J6, 306-555-0183, www.vault4keep.ca

Ad should inform the customer that we have:
-self storage with 24hr accesss
-pecialty storage products (seasonal bicycle, tire, and motorcycle storage),
-moving truck rental.
-online booking and payments

Ad should imply that we are safe, secure, and convenient.
Ad should have a clever tag line including the company name
This ad will be printed, and is not for web use.

Company logo is attached

```html
<!DOCTYPE html>
<html lang="en">
<head>
<meta charset="utf-8">
<title>Vault 4 Keep Storage – Folder Ad</title>
<link rel="stylesheet" href="https://fonts.googleapis.com/css2?family=Anton&family=Roboto:wght@400;700&display=swap">
<style>
  :root {
    --brand-red: #cc2a22;
    --ink: #141414;
    --edge: #333333;
    --paper: #ffffff;
    --backdrop: #e9e9e9;
  }
  * { margin: 0; padding: 0; box-sizing: border-box; }
  html, body { width: 1200px; height: 845px; overflow: hidden; background: var(--backdrop); }
  .ad {
    position: absolute; left: 67px; top: 143px;
    width: 1066px; height: 558px;
    background: var(--paper); overflow: hidden;
    font-family: "Roboto", Arial, sans-serif;
  }
  .ad__panel { position: absolute; inset: 0; }
  .brand {
    position: absolute; left: 20px; top: 150px; width: 290px;
    display: flex; align-items: center; justify-content: center; gap: 12px;
    color: var(--ink); font-weight: 700; font-size: 30px; line-height: 1.1;
    text-transform: uppercase; text-align: center;
  }
  .brand__mark { width: 20px; height: 20px; background: var(--brand-red); flex: none; }
  .contact {
    position: absolute; left: 75px; top: 356px;
    color: var(--ink); font-size: 25px; line-height: 31px;
  }
  .contact__phone { font-weight: 700; font-size: 27px; }
  .contact__web { color: var(--brand-red); }
  .headline {
    position: absolute; left: 434px; top: 36px;
    font-family: "Anton", Impact, sans-serif; font-size: 80px; line-height: 72px;
    text-transform: uppercase; letter-spacing: 0.5px;
  }
  .headline__dark { color: var(--ink); display: block; }
  .headline__light { color: var(--paper); display: block; }
  .services {
    position: absolute; left: 434px; top: 332px; list-style: none;
    color: var(--paper); font-size: 18px;
  }
  .services li { display: flex; align-items: flex-start; gap: 6px; margin-bottom: 10px; }
  .services li svg { flex: none; margin-top: 4px; }
  .services small { display: block; font-size: 11.5px; margin: 4px 0 0 12px; }
  .tagline {
    position: absolute; left: 434px; top: 495px;
    color: var(--paper); font-weight: 700; font-size: 18.5px; letter-spacing: 0.3px;
  }
</style>
</head>
<body>
<main class="ad">
  <svg class="ad__panel" width="1066" height="558" viewBox="0 0 1066 558" aria-hidden="true">
    <path d="M385 0 Q255 279 385 558" fill="none" stroke="var(--edge)" stroke-width="14"/>
    <path d="M392 0 Q262 279 392 558 L1066 558 L1066 0 Z" fill="var(--brand-red)"/>
  </svg>

  <div class="brand"><span class="brand__mark"></span><span>Vault 4 Keep<br>Storage</span></div>

  <address class="contact" style="font-style:normal">
    4817 Brenmor ave,<br>
    Saskatoon, SK,<br>
    S4N 2J6,<br>
    <span class="contact__phone">306-555-0183</span><br>
    <span class="contact__web">www.vault4keep.ca</span>
  </address>

  <h1 class="headline">
    <span class="headline__dark">Storage</span>
    <span class="headline__dark">Any Time</span>
    <span class="headline__light">Safety</span>
    <span class="headline__light">All Time</span>
  </h1>

  <ul class="services">
    <li><svg width="12" height="12" viewBox="0 0 12 12" aria-hidden="true"><circle cx="6" cy="6" r="6" fill="#fff"/><path d="M6 3 L6 9 M3.8 5.2 L6 3 L8.2 5.2" stroke="var(--brand-red)" stroke-width="1.6" fill="none"/></svg><span>Self storage with 24hr accesss</span></li>
    <li><svg width="12" height="12" viewBox="0 0 12 12" aria-hidden="true"><circle cx="6" cy="6" r="6" fill="#fff"/><path d="M6 3 L6 9 M3.8 5.2 L6 3 L8.2 5.2" stroke="var(--brand-red)" stroke-width="1.6" fill="none"/></svg><span>Pecialty storage products<small>(seasonal bicycle, tire, and motorcycle storage),</small></span></li>
    <li><svg width="12" height="12" viewBox="0 0 12 12" aria-hidden="true"><circle cx="6" cy="6" r="6" fill="#fff"/><path d="M6 3 L6 9 M3.8 5.2 L6 3 L8.2 5.2" stroke="var(--brand-red)" stroke-width="1.6" fill="none"/></svg><span>Moving truck rental.</span></li>
    <li><svg width="12" height="12" viewBox="0 0 12 12" aria-hidden="true"><circle cx="6" cy="6" r="6" fill="#fff"/><path d="M6 3 L6 9 M3.8 5.2 L6 3 L8.2 5.2" stroke="var(--brand-red)" stroke-width="1.6" fill="none"/></svg><span>Online booking and payments</span></li>
  </ul>

  <p class="tagline">WE ARE SAFE, SECURE, AND CONVENIENT.</p>
</main>
</body>
</html>
```